London based Blowdry bar needs drinks menu

Volara Blowdry Bar is a successful trendy 'Blowdry bar' based in London. We offer our clients a number of services that are quick, affordable and ideal for a perfect night out!
Within the salon we offer soft & alcoholic drinks - I need to advertise this but space is limited. Therefore I would like to have a simple but pretty bar menu that will be designed like a banner and run under the mirrors at each position.
Please look at our website to have a look inside salon and pick up design ideas, colours used and feel of salon.
Website = www.quickstylelounge.co.uk
Font used for Volara logo = Houschka rounded
Font used on website = District Pro
Measurement for each menu 90cm length x 7.5cm height (horizontal menu)
Target Market(s)
20-50 year olds - clients in salon to have a fast fun experience. needs to be clear, easy to read and to the point
Font styles to use
Other font styles liked:
- District Pro
Requirements
Must have
- Title of drink, price of drink - easy to read font
Nice to have
- Nice to have a picture of drink in beginning of menu (nice visual add) to draw attention to clients eyes and so they understand it is a drinks menu. Clear points at the beginning of each drink.

```html
<!DOCTYPE html>
<html lang="en">
<head>
<meta charset="utf-8">
<title>Volara Blowdry Bar – Drinks Menu</title>
<link rel="stylesheet" href="https://fonts.googleapis.com/css2?family=Quicksand:wght@400;500&display=swap">
<style>
  :root {
    --page-bg: #ffffff;
    --ink: #1c1a1d;
    --band-light: #f4f3f4;
    --band-mid: #efe4ec;
    --band-pink: #e6bfdc;
    --band-deep: #dfb0d4;
    --lime: #a9cf4a;
    --lime-deep: #5f9a2a;
    --glass: #e9efc8;
  }
  * { box-sizing: border-box; margin: 0; padding: 0; }
  html, body {
    width: 1200px;
    height: 184px;
    overflow: hidden;
    background: var(--page-bg);
  }
  .drinks-banner {
    position: absolute;
    left: 38px;
    top: 43px;
    width: 1124px;
    height: 93px;
    background:
      radial-gradient(ellipse 260px 70px at 760px 20px, rgba(230,191,220,0.55), transparent 70%),
      radial-gradient(ellipse 300px 90px at 1050px 70px, rgba(223,176,212,0.7), transparent 70%),
      linear-gradient(90deg, var(--band-light) 0%, var(--band-light) 30%, var(--band-mid) 55%, var(--band-pink) 80%, var(--band-deep) 100%);
    box-shadow: 0 1px 6px rgba(0,0,0,0.35);
    color: var(--ink);
  }
  .drink-illustration {
    position: absolute;
    left: 14px;
    top: 6px;
    width: 68px;
    height: 80px;
    border-radius: 10px;
    background: radial-gradient(circle at 40% 35%, var(--glass) 0%, var(--lime) 55%, var(--lime-deep) 100%);
    opacity: 0.85;
  }
  .banner-title {
    position: absolute;
    left: 94px;
    top: 34px;
    font-family: "Quicksand", sans-serif;
    font-weight: 400;
    font-size: 30px;
    line-height: 36px;
    white-space: nowrap;
  }
  .drink-column {
    position: absolute;
    top: 11px;
    list-style: none;
    font-family: "Quicksand", sans-serif;
    font-weight: 500;
    font-size: 12.5px;
    line-height: 15px;
    word-spacing: 0;
  }
  .drink-column li { margin-bottom: 12px; white-space: nowrap; }
  .drink-column li::before { content: "\2022"; }
  .drink-column .detail { display: block; padding-left: 7px; }
  .col-soft { left: 465px; }
  .col-wine { left: 686px; }
  .col-fizz { left: 896px; }
</style>
</head>
<body>
  <section class="drinks-banner" aria-label="Volara Blowdry Bar drinks menu">
    <div class="drink-illustration" role="img" aria-label="Watercolour margarita glass with lime slices"></div>
    <h1 class="banner-title">Why not have a drink?</h1>
    <ul class="drink-column col-soft">
      <li>Filtered Water</li>
      <li>Sparkling Water £1.50</li>
      <li>Cola / Diet Cola £2</li>
    </ul>
    <ul class="drink-column col-wine">
      <li>100% real Fruit Juice £2</li>
      <li>Dry White Wine /<span class="detail">Red Wine £4</span></li>
    </ul>
    <ul class="drink-column col-fizz">
      <li>Prosecco / Rose Prosecco £5</li>
      <li>Prosecco Cocktails<span class="detail">Choose from Elderflower, Peach,</span><span class="detail">Spritz &amp; Hibiscus – £7</span></li>
    </ul>
  </section>
</body>
</html>
```